Business Card Design

Locksmith, Safes, Security Systems, Camera Systems, Home Theater, Chip Keys & Remotes

Industry/Entity Type

Business

Contact Information for Business Card

Dorian Pelley Owner
2870 Fenwick Hollow Loop
Dothan, AL 36301
P 334-555-0148
F 334-555-0193
dpelley@tamblynkeys.com
www.tamblynkeys.com
AL Lic #5827
*Maybe follow us on Facebook or Facebook symbol

```html
<!DOCTYPE html>
<html lang="en">
<head>
<meta charset="utf-8">
<title>Tamblyn's Lock &amp; Security – Business Card</title>
<link rel="stylesheet" href="https://fonts.googleapis.com/css2?family=PT+Sans+Narrow:wght@400;700&display=swap">
<style>
  :root {
    --band: #dcdcef;
    --stripe: #b8bbe1;
    --paper: #ffffff;
    --brand-blue: #2b46a3;
    --ink: #2e2e33;
    --licence: #b4b8de;
    --icon-bg: #e3e4f3;
  }
  * { margin: 0; padding: 0; box-sizing: border-box; }
  html, body { width: 1200px; height: 692px; overflow: hidden; background: var(--paper); }
  .card {
    position: relative;
    width: 1200px;
    height: 692px;
    background: var(--paper);
    font-family: "PT Sans Narrow", "Arial Narrow", sans-serif;
    overflow: hidden;
  }
  .top-band {
    position: absolute; left: 0; top: 0;
    width: 100%; height: 404px;
    background: var(--band);
  }
  .divider-stripe {
    position: absolute; left: 0; top: 404px;
    width: 100%; height: 22px;
    background: var(--stripe);
  }
  .brand-mark {
    position: absolute; left: 57px; top: 54px;
    width: 160px; height: 232px;
    background: var(--brand-blue);
    border-radius: 10px;
  }
  .brand-name {
    position: absolute; left: 270px; top: 112px;
    color: var(--brand-blue);
    font-weight: 700;
    text-transform: uppercase;
    line-height: 1;
  }
  .brand-name .primary { display: block; font-size: 74px; letter-spacing: 1px; }
  .brand-name .secondary { display: block; font-size: 34px; letter-spacing: 2px; margin: 10px 0 0 48px; }
  .services {
    position: absolute; left: 270px; top: 292px;
    width: 720px;
    font-size: 36px;
    line-height: 44px;
    color: var(--ink);
  }
  .contact {
    position: absolute; left: 270px; top: 448px;
    font-size: 35px;
    line-height: 45px;
    color: var(--brand-blue);
    list-style: none;
  }
  .contact li { position: relative; white-space: nowrap; }
  .contact .icon {
    position: absolute; left: -50px; top: 11px;
    width: 24px; height: 24px;
  }
  .licence {
    position: absolute; right: 44px; top: 633px;
    font-size: 33px;
    color: var(--licence);
  }
</style>
</head>
<body>
  <div class="card">
    <div class="top-band"></div>
    <div class="divider-stripe"></div>

    <div class="brand-mark"></div>
    <div class="brand-name">
      <span class="primary">Tamblyn's</span>
      <span class="secondary">Lock &amp; Security</span>
    </div>

    <p class="services">Locksmith, Safes, Security Systems, Camera Systems, Home Theater, Chip Keys &amp; Remotes</p>

    <ul class="contact">
      <li>Dorian Pelley Owner</li>
      <li>2870 Fenwick Hollow Loop Dothan,</li>
      <li>AL 36301 P 334-555-0148 F 334-555-0193</li>
      <li>
        <svg class="icon" viewBox="0 0 24 24" aria-hidden="true">
          <circle cx="12" cy="12" r="12" fill="var(--icon-bg)"/>
          <rect x="6" y="8" width="12" height="8.5" rx="1" fill="none" stroke="var(--brand-blue)" stroke-width="1.6"/>
          <path d="M6.5 8.7 L12 13 L17.5 8.7" fill="none" stroke="var(--brand-blue)" stroke-width="1.6"/>
        </svg>
        dpelley@tamblynkeys.com
      </li>
      <li>
        <svg class="icon" viewBox="0 0 24 24" aria-hidden="true">
          <circle cx="12" cy="12" r="12" fill="var(--icon-bg)"/>
          <circle cx="12" cy="12" r="5.5" fill="none" stroke="var(--brand-blue)" stroke-width="1.6"/>
          <path d="M6.5 12 H17.5 M12 6.5 C9.5 9.5 9.5 14.5 12 17.5 M12 6.5 C14.5 9.5 14.5 14.5 12 17.5" fill="none" stroke="var(--brand-blue)" stroke-width="1.2"/>
        </svg>
        www.tamblynkeys.com
      </li>
    </ul>

    <div class="licence">AL Lic #5827</div>
  </div>
</body>
</html>
```